Industrial Laundry News Paper Add

We need a color add for 1/4 page newspaper using blue and white. We are an industrial laundry providing linen washing for condo rental companies. We can provide linen rental and wash customer-owned goods

```html
<!DOCTYPE html>
<html lang="en">
<head>
<meta charset="utf-8">
<title>Summit Ridge Services – Industrial Laundry Ad</title>
<link href="https://fonts.googleapis.com/css2?family=Raleway:wght@400;500;600;700;800&display=swap" rel="stylesheet">
<style>
  :root {
    --navy: #1d1a4f;
    --blue: #5670a6;
    --white: #ffffff;
    --ink: #1a1a1a;
    --backdrop: #c3c4c6;
  }
  * { margin: 0; padding: 0; box-sizing: border-box; }
  html, body { width: 1044px; height: 1200px; overflow: hidden; }
  body {
    background: var(--backdrop);
    font-family: "Raleway", sans-serif;
    position: relative;
  }
  .ad {
    position: absolute;
    left: 209px; top: 135px;
    width: 606px; height: 945px;
    background: var(--white);
    overflow: hidden;
  }
  .ad__art { position: absolute; left: 0; top: 0; width: 606px; height: 545px; }
  .ad__call {
    position: absolute; right: 18px; top: 30px;
    color: var(--white); font-weight: 700; font-size: 15.5px;
    line-height: 20px; text-align: right;
  }
  .brand {
    position: absolute; left: 389px; top: 476px; width: 200px;
    text-align: center;
  }
  .brand__name {
    color: var(--navy); font-weight: 700; font-size: 18px; line-height: 19px;
  }
  .brand__tagline {
    margin-top: 3px;
    font-size: 7.5px; font-weight: 600; color: var(--blue); letter-spacing: .2px;
    white-space: nowrap;
  }
  .headline {
    position: absolute; right: 25px; top: 533px;
    color: var(--navy); font-weight: 800; font-size: 36.5px;
    line-height: 44px; text-align: right; letter-spacing: -.3px;
  }
  .intro {
    position: absolute; left: 39px; top: 645px; width: 338px;
    color: var(--ink); font-size: 15.8px; line-height: 19.4px; font-weight: 500;
  }
  .bubble { position: absolute; border-radius: 50%; }
  .bubble--back { left: 476px; top: 623px; width: 104px; height: 104px; background: var(--blue); }
  .bubble--small { left: 387px; top: 761px; width: 68px; height: 68px; background: var(--blue); }
  .bubble--main {
    left: 402px; top: 651px; width: 176px; height: 176px; background: var(--navy);
    display: flex; align-items: center; justify-content: center; text-align: center;
    color: var(--white); font-weight: 700; font-size: 15.5px; line-height: 19.5px; padding: 0 24px;
  }
  .contact-bar {
    position: absolute; left: 0; top: 860px; width: 606px; height: 24px;
    background: var(--blue); color: var(--white);
    font-weight: 700; font-size: 15px; line-height: 24px; padding-left: 39px;
  }
  .footer {
    position: absolute; left: 0; top: 884px; width: 606px; height: 61px;
    background: var(--navy); color: var(--white);
  }
  .footer__details { position: absolute; left: 39px; top: 13px; font-size: 12.8px; line-height: 16.5px; font-weight: 500; }
  .footer__follow { position: absolute; left: 486px; top: 4px; font-size: 15px; font-weight: 700; }
  .footer__social { position: absolute; left: 487px; top: 27px; display: flex; gap: 5px; }
  .footer__social span { width: 16px; height: 16px; border-radius: 50%; background: var(--white); }
</style>
</head>
<body>
  <article class="ad">
    <svg class="ad__art" viewBox="0 0 606 545">
      <defs>
        <linearGradient id="machines" x1="0" y1="0" x2="1" y2="1">
          <stop offset="0" stop-color="#9a9ea4"/>
          <stop offset=".45" stop-color="#dfe2e5"/>
          <stop offset="1" stop-color="#7d8187"/>
        </linearGradient>
      </defs>
      <polygon role="img" aria-label="Photo of a row of industrial washing machines" points="0,0 330,0 606,200 606,375 255,450 0,383" fill="url(#machines)"/>
      <polygon points="360,0 606,0 606,190" fill="var(--navy)"/>
      <polygon points="378,0 606,0 606,174" fill="var(--blue)"/>
      <polygon points="0,383 255,450 0,505" fill="var(--navy)"/>
      <polygon points="0,505 606,377 606,394 0,540" fill="var(--blue)"/>
    </svg>

    <p class="ad__call">CALL US:<br>+1.5550147200</p>

    <div class="brand">
      <p class="brand__name">SUMMIT RIDGE<br>SERVICES</p>
      <p class="brand__tagline">HOUSKEEPING•LAUNDRY•CARPET CLEANING</p>
    </div>

    <h1 class="headline">THE FIRST NAME<br>IN INDUSTRIAL LAUNDRY</h1>

    <p class="intro">Summit Ridge Services is a family-owned and operated cleaning company. Our goal is to continued growth by offering customers a consistent, reliable total cleaning solution day in and day out. We always strive to combine industry experience with the latest cleaning technologies and environmentally friendly products — so you get the best possible results.</p>

    <div class="bubble bubble--back"></div>
    <div class="bubble bubble--small"></div>
    <div class="bubble bubble--main">We can provide linen rental and wash customer&#8209;owned goods</div>

    <div class="contact-bar">CONTACT US FOR MORE INFORMATION</div>
    <footer class="footer">
      <p class="footer__details">+1.5550147200 &nbsp;|&nbsp; www.summitridgeservices.com<br>Alpine Crest Partners, Inc. Pine Hollow, CA 90000, USA</p>
      <p class="footer__follow">FOLLOW US</p>
      <div class="footer__social"><span></span><span></span><span></span></div>
    </footer>
  </article>
</body>
</html>
```